Anzeigengestaltung für Bernhardinerzucht
Unkomplizierte Zusammenarbeit, der erste Entwurf hat bis auf kleine Änderungswünsche sofort gefallen.
Zielgruppe
Ich bin neu in der Bernhardinerzucht und möchte auf mich aufmerksam machen. Wir haben Anfang März unseren ersten A - Wurf Bernhardiner bekommen.
Unsere Zielgruppe sind interessierte Käufer der Rasse und andere Züchter.
Aufgabenstellung
Wir haben hübsche Welpen aus der Verpaarung von :
Rüde:
Bruno vom Haldenmoor
Hündin :
Elsa-Mai vom Haldenfeld
Die drei Rüden wurden am 6. März geboren. Sie sind Mitte Mai geimpft, mehrfach entwurmt und gechipt abgabebereit.
Kurze Beschreibung
Wir sind eine kleine Zuchtstätte.
Unser Ziel ist es, mit viel Liebe wesensfeste, gesunde und möglichst langlebige Bernhardiner
zu züchten.
Format DIN A6 ist eine halbe Seite eines Zuchtkatalog für eine Spezialzuchtschau Bernhardiner
Bitte bei den Bildern möglichst nur den Oberkörper/Kopf verwenden. Es sind zwei Bilder der Hündin und ein Bild des Rüden (Bruno vom Haldenmoor) verfügbar.

```html
<!DOCTYPE html>
<html lang="de">
<head>
<meta charset="utf-8">
<title>Bernhardinerzucht vom oberen Talgrund – Anzeige</title>
<link rel="stylesheet" href="https://fonts.googleapis.com/css2?family=Bitter:wght@400;500&family=Ubuntu:wght@500;700&display=swap">
<style>
  :root {
    --teal-light: #3e6669;
    --teal-mid: #34595d;
    --teal-dark: #27494d;
    --white: #ffffff;
    --gold: #c08a2c;
    --label-gold: #cfa86a;
    --coat-brown: #9c5a2a;
    --coat-white: #ece2d4;
  }
  * { margin: 0; padding: 0; box-sizing: border-box; }
  html, body { width: 1200px; height: 851px; overflow: hidden; }
  body { background: var(--teal-dark); }

  .ad {
    position: relative;
    width: 1200px;
    height: 851px;
    overflow: hidden;
    color: var(--white);
    background:
      radial-gradient(ellipse at 80% 60%, rgba(255,255,255,0.06), transparent 55%),
      linear-gradient(180deg, var(--teal-light) 0%, var(--teal-mid) 50%, var(--teal-dark) 100%);
  }

  .kennel-title {
    position: absolute;
    right: 62px;
    top: 46px;
    text-align: right;
  }
  .kennel-name {
    font-family: "Bitter", serif;
    font-weight: 400;
    font-size: 50px;
    line-height: 1;
    letter-spacing: 0.02em;
  }
  .kennel-type {
    font-family: "Ubuntu", sans-serif;
    font-weight: 700;
    font-size: 36px;
    letter-spacing: 0.36em;
    margin-right: -0.36em;
    line-height: 1;
    margin-top: 10px;
  }

  .headline {
    position: absolute;
    left: 79px;
    top: 236px;
    font-family: "Ubuntu", sans-serif;
    font-weight: 700;
    font-size: 28px;
    line-height: 35px;
    color: var(--gold);
    letter-spacing: 0.01em;
  }

  .copy {
    position: absolute;
    left: 79px;
    width: 460px;
    font-family: "Bitter", serif;
    font-weight: 500;
    font-size: 20.5px;
    line-height: 24px;
    letter-spacing: 0.02em;
  }
  .copy--litter { top: 352px; }
  .copy--kennel { top: 472px; }

  .breeder {
    position: absolute;
    left: 79px;
    top: 705px;
  }
  .breeder-name {
    font-family: "Bitter", serif;
    font-size: 24px;
    letter-spacing: 0.34em;
    line-height: 1;
    margin-bottom: 12px;
  }
  .breeder-contact {
    font-family: "Ubuntu", sans-serif;
    font-weight: 500;
    font-size: 20px;
    line-height: 24px;
    letter-spacing: 0.02em;
  }

  .dog-photo {
    position: absolute;
    border-radius: 46% 46% 20% 20% / 30% 30% 12% 12%;
    background: linear-gradient(160deg, var(--coat-brown) 0%, #b77a44 35%, var(--coat-white) 70%, #d9ccb9 100%);
    opacity: 0.9;
  }
  .dog-photo--female { left: 584px; top: 248px; width: 230px; height: 460px; }
  .dog-photo--male {
    left: 752px; top: 385px; width: 428px; height: 430px;
    border-radius: 30% 40% 14% 14% / 24% 30% 10% 10%;
    background: linear-gradient(150deg, #f0e6d8 0%, var(--coat-brown) 30%, #b06f35 60%, var(--coat-white) 100%);
  }

  .dog-label {
    position: absolute;
    font-family: "Bitter", serif;
    font-weight: 500;
    font-size: 18px;
    line-height: 21px;
    color: var(--label-gold);
    letter-spacing: 0.02em;
  }
  .dog-label--female { left: 827px; top: 278px; }
  .dog-label--male { left: 906px; top: 737px; }
</style>
</head>
<body>
  <main class="ad">
    <header class="kennel-title">
      <h1 class="kennel-name">vom oberen Talgrund</h1>
      <p class="kennel-type">St. Bernhards-Zwinger</p>
    </header>

    <h2 class="headline">Wir haben hübsche Welpen<br>aus der Verpaarung von:</h2>

    <p class="copy copy--litter">Die drei Rüden wurden am 6. März geboren. Sie sind Mitte Mai geimpft, mehrfach entwurmt und gechipt abgabebereit.</p>

    <p class="copy copy--kennel">Wir sind eine kleine Zuchtstätte. Unser Ziel ist es, mit viel Liebe wesensfeste, gesunde und möglichst langlebige Bernhardiner zu züchten.</p>

    <section class="breeder">
      <p class="breeder-name">Merle Soltau</p>
      <p class="breeder-contact">Lindenhang 7 | 36299 Birkental<br>0170/5518203 |merle.soltau@postfeld.de</p>
    </section>

    <div class="dog-photo dog-photo--female" role="img" aria-label="Foto der sitzenden Bernhardiner-Hündin Elsa-Mai vom Haldenfeld"></div>
    <div class="dog-photo dog-photo--male" role="img" aria-label="Foto des stehenden Bernhardiner-Rüden Bruno vom Haldenmoor"></div>

    <p class="dog-label dog-label--female">Elsa-Mai vom<br>&nbsp;Haldenfeld<br>&nbsp;Hündin</p>
    <p class="dog-label dog-label--male">Bruno vom<br>Haldenmoor<br>Rüde</p>
  </main>
</body>
</html>
```